RTV Photography Business Card Design

I would like a business card designed in the shape of a camera.
Would like to see various camera designs. Would like to see what the card looks like in different colors. Would like to see which logo looks better on the various camera designs so please show me some with the white logo and some with the black logo. If you need a different file formats please let me know.
Project Deadline Extended Reason: My grandfather passed away and dealing with funeral plans so need to extend deadline. Added Tuesday, March 1, 2016
Project Deadline Extended
Reason: I just got back from out of town. My grandfather's passing was the primary focus for me these past few weeks and the funeral is over so now I will concentrate on picking my business card design. I really appreciate each designer who has taken the time to submit a design. Your effort has not gone unnoticed. I look forward to seeing more amazing designs.
Industry/Entity Type
Business
Contact Information for Business Card
Wren
757-418-2096
https://www.facebook.com/rtvphotographyfreelance/
DoraWren@rtv-photography.example
Look and feel

```html
<!DOCTYPE html>
<html lang="en">
<head>
<meta charset="utf-8">
<title>RTV Photography – Business Card</title>
<link rel="stylesheet" href="https://fonts.googleapis.com/css2?family=Cinzel:wght@400&family=Montserrat:wght@400;600;700&display=swap">
<style>
  :root {
    --page-bg: #dedede;
    --card-bg: #000000;
    --lens-ring: #2a2a2a;
    --lens-core-light: #3a3a3a;
    --lens-core-dark: #060606;
    --flash-light: #e4e4e4;
    --flash-dark: #a9a9a9;
    --flash-edge: #cfcfcf;
    --gold: #d9a832;
    --text-white: #ffffff;
    --divider: #7a7a7a;
  }
  * { margin: 0; padding: 0; box-sizing: border-box; }
  html, body {
    width: 688px;
    height: 1200px;
    overflow: hidden;
    background: var(--page-bg);
  }
  .canvas {
    position: relative;
    width: 688px;
    height: 1200px;
  }
  .card {
    position: absolute;
    left: 44px;
    width: 600px;
    height: 341px;
    background: var(--card-bg);
    border-radius: 22px;
    overflow: hidden;
  }
  .card--front { top: 222px; }
  .card--back  { top: 636px; }

  .lens {
    position: absolute;
    left: 82px;
    top: 44px;
    width: 254px;
    height: 254px;
  }
  .flash {
    position: absolute;
    width: 135px;
    height: 67px;
    border-radius: 7px;
    border: 1px solid var(--flash-edge);
    background: linear-gradient(160deg, var(--flash-light) 0%, #c4c4c4 55%, var(--flash-dark) 100%);
  }
  .card--front .flash { left: 418px; top: 46px; }
  .card--back .flash  { left: 45px;  top: 45px; }

  .brand-mark {
    position: absolute;
    border-radius: 50%;
    background: var(--gold);
  }
  .brand-name {
    position: absolute;
    font-family: "Cinzel", serif;
    font-weight: 400;
    color: var(--gold);
    white-space: nowrap;
    text-align: center;
  }
  .card--front .brand-mark { left: 434px; top: 207px; width: 60px; height: 60px; }
  .card--front .brand-name {
    left: 364px; top: 275px; width: 200px;
    font-size: 17px; letter-spacing: 0.2px;
  }
  .card--back .brand-mark { left: 248px; top: 50px; width: 104px; height: 104px; }
  .card--back .brand-name {
    left: 100px; top: 164px; width: 400px;
    font-size: 31px; letter-spacing: 0.3px;
  }

  .person {
    position: absolute;
    right: 325px;
    top: 250px;
    text-align: right;
    font-family: "Montserrat", sans-serif;
    color: var(--text-white);
  }
  .person__name {
    font-size: 17px;
    font-weight: 700;
    letter-spacing: 0.6px;
    line-height: 22px;
  }
  .person__role {
    font-size: 14px;
    font-weight: 400;
    letter-spacing: 0.4px;
    line-height: 20px;
  }
  .divider {
    position: absolute;
    left: 298px;
    top: 221px;
    width: 1px;
    height: 97px;
    background: var(--divider);
  }
  .contact {
    position: absolute;
    left: 323px;
    top: 234px;
    list-style: none;
    font-family: "Montserrat", sans-serif;
    font-size: 14.5px;
    font-weight: 400;
    letter-spacing: 0.5px;
    line-height: 25px;
    color: var(--text-white);
  }
</style>
</head>
<body>
<main class="canvas">

  <section class="card card--front" aria-label="Card front">
    <svg class="lens" viewBox="0 0 254 254" aria-hidden="true">
      <defs>
        <radialGradient id="lens-core" cx="50%" cy="42%" r="60%">
          <stop offset="0%" stop-color="var(--lens-core-light)"/>
          <stop offset="100%" stop-color="var(--lens-core-dark)"/>
        </radialGradient>
      </defs>
      <circle cx="127" cy="127" r="127" fill="var(--lens-ring)"/>
      <circle cx="127" cy="127" r="105" fill="url(#lens-core)"/>
    </svg>
    <div class="flash"></div>
    <div class="brand-mark"></div>
    <div class="brand-name">RTV PHOTOGRAPHY</div>
  </section>

  <section class="card card--back" aria-label="Card back">
    <div class="flash"></div>
    <div class="brand-mark"></div>
    <div class="brand-name">RTV PHOTOGRAPHY</div>
    <div class="person">
      <p class="person__name">FIRSTNAME LASTNAME</p>
      <p class="person__role">PHOTOGRAPHER</p>
    </div>
    <div class="divider"></div>
    <ul class="contact">
      <li>123-456-7890</li>
      <li>info@rtv-photography.example</li>
      <li>www.rtv-photography.example</li>
    </ul>
  </section>

</main>
</body>
</html>
```